Criação de Logo + Papelaria + Manual Básico para Ventrona & Solmar
" Atendemos os clientes de forma consultiva, procurando no mercado as tecnologias mais adequadas para a otimização e estabilidade de redes corporativas. Somos parceiros homologados dos principais fabricantes do mercado, além de mantermos parcerias estratégicas para complementar nossas soluções com todas as competências necessárias. "

```html
<!DOCTYPE html>
<html lang="pt-BR">
<head>
<meta charset="UTF-8">
<title>Ventrona &amp; Solmar — Cartão de visita</title>
<link href="https://fonts.googleapis.com/css2?family=Exo+2:wght@400;600;700&display=swap" rel="stylesheet">
<style>
  :root{
    --bg:#f2f2f2;
    --navy:#111d29;
    --navy-soft:#16232f;
    --cyan:#2bb3d3;
    --white:#ffffff;
    --muted:#9aa6b2;
  }
  html,body{margin:0;padding:0;overflow:hidden;}
  body{width:1200px;height:1200px;background:var(--bg);font-family:"Exo 2",sans-serif;position:relative;}
  .card{position:absolute;left:278px;width:645px;height:400px;background:var(--navy);overflow:hidden;}
  .card--front{top:120px;}
  .card--back{top:680px;background:var(--navy-soft);}
  .edge-bar{position:absolute;width:14px;background:var(--cyan);}
  .card--front .edge-bar--left{left:0;top:30px;bottom:30px;}
  .card--front .edge-bar--right{right:0;top:90px;bottom:60px;}
  .card--back .edge-bar--left{left:0;top:20px;bottom:190px;}
  .card--back .edge-bar--right{right:0;top:20px;bottom:90px;}
  .brand{display:flex;align-items:center;gap:12px;color:var(--white);font-weight:700;font-size:34px;letter-spacing:.5px;white-space:nowrap;}
  .brand__dot{width:18px;height:18px;border-radius:50%;background:var(--cyan);}
  .card--front .brand{position:absolute;left:50%;top:50%;transform:translate(-50%,-50%);}
  .card--back .brand{position:absolute;left:40px;top:170px;font-size:30px;}
  .contact{position:absolute;right:42px;top:95px;text-align:right;color:var(--white);}
  .contact__name{font-size:27px;font-weight:700;margin:0;line-height:1.1;}
  .contact__role{font-size:14px;color:var(--muted);margin:0 0 14px;}
  .contact__list{list-style:none;margin:0;padding:0;}
  .contact__item{display:flex;justify-content:flex-end;align-items:center;gap:12px;font-size:15px;font-weight:600;height:31px;}
  .contact__icon{width:18px;height:18px;fill:none;stroke:var(--white);stroke-width:2;stroke-linecap:round;stroke-linejoin:round;}
</style>
</head>
<body>
  <section class="card card--front">
    <span class="edge-bar edge-bar--left"></span>
    <span class="edge-bar edge-bar--right"></span>
    <div class="brand"><span class="brand__dot"></span>Ventrona &amp; Solmar</div>
  </section>

  <section class="card card--back">
    <span class="edge-bar edge-bar--left"></span>
    <span class="edge-bar edge-bar--right"></span>
    <div class="brand"><span class="brand__dot"></span>Ventrona &amp; Solmar</div>
    <div class="contact">
      <p class="contact__name">Nome Sobrenome</p>
      <p class="contact__role">cargo</p>
      <ul class="contact__list">
        <li class="contact__item">+55 11 9 9999-8888
          <svg class="contact__icon" viewBox="0 0 24 24"><path d="M5 3h4l2 5-3 2a12 12 0 0 0 6 6l2-3 5 2v4a2 2 0 0 1-2 2A17 17 0 0 1 3 5a2 2 0 0 1 2-2z"/></svg></li>
        <li class="contact__item">+55 11 9 9999-8888
          <svg class="contact__icon" viewBox="0 0 24 24"><rect x="6" y="2" width="12" height="20" rx="2"/><path d="M11 18h2"/></svg></li>
        <li class="contact__item">contato@ventronasolmar.com.br
          <svg class="contact__icon" viewBox="0 0 24 24"><rect x="3" y="5" width="18" height="14" rx="1"/><path d="M3 6l9 7 9-7"/></svg></li>
        <li class="contact__item">www.ventronasolmar.com.br
          <svg class="contact__icon" viewBox="0 0 24 24"><circle cx="12" cy="12" r="9"/><path d="M3 12h18M12 3c3 3 3 15 0 18M12 3c-3 3-3 15 0 18"/></svg></li>
        <li class="contact__item">Endereço: Exemplo - Exemplo
          <svg class="contact__icon" viewBox="0 0 24 24"><path d="M12 22s7-7 7-12a7 7 0 0 0-14 0c0 5 7 12 7 12z"/><circle cx="12" cy="10" r="2.5"/></svg></li>
      </ul>
    </div>
  </section>
</body>
</html>
```